Business Intelligence/Analytics Technology Company Business Card

We are a higher-end enterprise software development company working with Retailer POS data to provide business intelligence and analytical services to fortune 500 companies.

I have an immediate need for a professional/thick/bold business card. The same design aspects will spiral into more media such as flyers/folders/etc...

Our website is www.brenvolq.com for our product.

I like "Clean" designs if that makes sense, not a lot of "stuff".

The uploaded files, the A logo with the box is the style we're leaning towards, but the A logo without the blue box is all good too... get creative.

Target Market(s)

Executives of large companies, down to VP level..

Industry/Entity Type

Software

Requirements
Must have
• I'm wanting a thick designer like business card.

I think we're going to change our logo to a more quillmesh 8 looking style... http://www.brenvolq.com/card.ai as an example of our current business card.

The winner will also have knowledge of where i can get these things printed.
Nice to have
• Blue-ish color scheme? I'm open to anything. Our Competition is Red, and another is Green. So we'll stick with the Blue.

```html
<!DOCTYPE html>
<html lang="en">
<head>
<meta charset="utf-8">
<title>Brenvolq Business Card</title>
<link rel="stylesheet" href="https://fonts.googleapis.com/css2?family=Open+Sans:wght@400;600;700&display=swap">
<style>
  :root {
    --blue-light: #1c7cc4;
    --blue-mid: #0f5ea8;
    --blue-deep: #0b3f86;
    --grey-band: #b9bcc2;
    --card-white: #ffffff;
    --ink-dark: #2b2f36;
    --ink-soft: #e6eef8;
    --page-bg: #eceef1;
  }
  * { margin: 0; padding: 0; box-sizing: border-box; }
  html, body { width: 1200px; height: 900px; overflow: hidden; }
  body {
    background: var(--page-bg);
    font-family: "Open Sans", Arial, sans-serif;
    position: relative;
  }
  .card {
    position: absolute;
    left: 285px;
    width: 630px;
    height: 360px;
    overflow: hidden;
    box-shadow: 0 6px 18px rgba(0,0,0,0.18);
  }
  .card--front {
    top: 70px;
    background: linear-gradient(135deg, var(--blue-light) 0%, var(--blue-mid) 45%, var(--blue-deep) 100%);
    color: var(--card-white);
  }
  .card--back { top: 470px; background: var(--card-white); }

  .brand { position: absolute; display: flex; flex-direction: column; }
  .brand__row { display: flex; align-items: center; gap: 14px; }
  .brand__square { width: 26px; height: 26px; flex: none; }
  .brand__name {
    font-weight: 600;
    font-size: 40px;
    letter-spacing: 14px;
    line-height: 1;
    white-space: nowrap;
  }
  .brand__tagline {
    font-weight: 700;
    font-size: 14px;
    margin-top: 8px;
    margin-left: 40px;
    white-space: nowrap;
  }
  .card--front .brand { left: 150px; top: 130px; }
  .card--front .brand__square { background: var(--card-white); }
  .card--front .brand__name, .card--front .brand__tagline { color: var(--card-white); }
  .front__url {
    position: absolute;
    left: 300px;
    top: 250px;
    font-size: 16px;
    letter-spacing: 0.5px;
  }

  .back__shape { position: absolute; inset: 0; }
  .card--back .brand { left: 36px; top: 160px; }
  .card--back .brand__row { gap: 11px; }
  .card--back .brand__square { width: 22px; height: 22px; background: var(--blue-mid); }
  .card--back .brand__name, .card--back .brand__tagline { color: var(--ink-dark); }
  .card--back .brand__name { font-size: 28px; letter-spacing: 8px; }
  .card--back .brand__tagline { font-size: 11px; margin-left: 33px; margin-top: 6px; }

  .contact {
    position: absolute;
    right: 26px;
    top: 22px;
    width: 230px;
    text-align: right;
    color: var(--card-white);
    font-size: 11.5px;
    line-height: 1.45;
  }
  .contact__name { font-weight: 700; font-size: 17px; line-height: 1.2; }
  .contact__title { font-weight: 600; font-size: 12px; margin-bottom: 10px; }
  .contact__address { margin-bottom: 12px; color: var(--ink-soft); }
  .contact__lines { list-style: none; color: var(--ink-soft); }
  .contact__lines li { display: flex; justify-content: flex-end; align-items: center; gap: 6px; }
  .contact__lines svg { width: 11px; height: 11px; fill: var(--ink-soft); }
  .contact__url { margin-top: 12px; font-size: 12px; }
</style>
</head>
<body>

<section class="card card--front">
  <div class="brand">
    <div class="brand__row">
      <span class="brand__square"></span>
      <span class="brand__name">BRENVOLQ</span>
    </div>
    <span class="brand__tagline">Brenvolq . Lumen . Retail health</span>
  </div>
  <p class="front__url">www.brenvolq.com</p>
</section>

<section class="card card--back">
  <svg class="back__shape" viewBox="0 0 630 360" width="630" height="360">
    <defs>
      <linearGradient id="bandBlue" x1="0" y1="0" x2="1" y2="1">
        <stop offset="0" stop-color="var(--blue-light)"/>
        <stop offset="1" stop-color="var(--blue-deep)"/>
      </linearGradient>
    </defs>
    <path d="M372,0 C318,120 318,240 372,360 L630,360 L630,0 Z" fill="var(--grey-band)"/>
    <path d="M388,0 C336,120 336,240 388,360 L630,360 L630,0 Z" fill="url(#bandBlue)"/>
  </svg>

  <div class="brand">
    <div class="brand__row">
      <span class="brand__square"></span>
      <span class="brand__name">BRENVOLQ</span>
    </div>
    <span class="brand__tagline">Brenvolq . Lumen . Retail health</span>
  </div>

  <div class="contact">
    <p class="contact__name">Dana Morrell</p>
    <p class="contact__title">Business Director</p>
    <p class="contact__address">Brenvolq Technology Group, Inc<br>1450 Harlow Ave<br>Suite 210<br>Fenwick, AR 72014</p>
    <ul class="contact__lines">
      <li><svg viewBox="0 0 12 12"><path d="M2 1h3l1 3-1.5 1a7 7 0 0 0 2.5 2.5L8 6l3 1v3a1 1 0 0 1-1 1A9 9 0 0 1 1 2a1 1 0 0 1 1-1z"/></svg>555.210.4481</li>
      <li><svg viewBox="0 0 12 12"><path d="M1 3h10v7H1z M3 1h6v2H3z"/></svg>555.210.4490</li>
      <li><svg viewBox="0 0 12 12"><path d="M3 0h6a1 1 0 0 1 1 1v10a1 1 0 0 1-1 1H3a1 1 0 0 1-1-1V1a1 1 0 0 1 1-1zm0 2v7h6V2z"/></svg>555.318.7022</li>
      <li><svg viewBox="0 0 12 12"><path d="M0 2h12v8H0zm1 1v.5l5 3 5-3V3z"/></svg>dana@brenvolq.com</li>
    </ul>
    <p class="contact__url">www.brenvolq.com</p>
  </div>
</section>

</body>
</html>
```